Professional/Sleek card design for athletic apparel brand

Athletic apparel brand. Mainly focused on lifting weights/gym workouts. Logo and brand are already created. Must use brand logo and name. Creativity is welcome. Looking for a clean, modern, and sexy design.

```html
<!DOCTYPE html>
<html lang="en">
<head>
<meta charset="utf-8">
<title>Iron and Grit — Business Card</title>
<link href="https://fonts.googleapis.com/css2?family=Exo+2:wght@600;700;800&family=Questrial&display=swap" rel="stylesheet">
<style>
  :root {
    --backdrop: #8f8f8f;
    --card-dark: #2a2a2a;
    --card-dark-deep: #1f1f1f;
    --card-light: #f1f1f1;
    --ink: #1e1e1e;
    --ink-soft: #6e6e6e;
    --brand-grey: #9b9b9b;
    --emboss: #171717;
  }
  * { box-sizing: border-box; margin: 0; padding: 0; }
  html, body { width: 1200px; height: 1200px; overflow: hidden; }
  body { background: var(--backdrop); position: relative; font-family: "Questrial", sans-serif; }

  .card {
    position: absolute;
    top: 266px;
    width: 436px;
    height: 746px;
    border-radius: 25px;
    overflow: hidden;
  }

  /* Back side */
  .card--back { left: 162px; background: var(--card-dark); }
  .back__pattern {
    position: absolute;
    left: 0; top: 0;
    width: 436px; height: 520px;
    background:
      radial-gradient(ellipse 70% 60% at 40% 45%, rgba(18,18,18,0.75), rgba(18,18,18,0) 100%),
      linear-gradient(180deg, var(--card-dark-deep) 0%, var(--card-dark) 100%);
  }
  .back__word {
    position: absolute;
    left: 0; right: 0;
    text-align: center;
    font-family: "Exo 2", sans-serif;
    font-weight: 800;
    color: var(--emboss);
    line-height: 1;
  }
  .back__word--top { top: 520px; font-size: 80px; letter-spacing: 8px; }
  .back__word--bottom { top: 645px; font-size: 80px; letter-spacing: 8px; }
  .back__divider {
    position: absolute;
    left: 12px; right: 17px; top: 618px;
    display: flex; align-items: center; gap: 14px;
    font-family: "Exo 2", sans-serif; font-weight: 800;
    font-size: 22px; line-height: 22px; letter-spacing: 6px;
    color: var(--emboss);
  }
  .back__divider::before, .back__divider::after {
    content: ""; flex: 1; height: 3px; background: var(--emboss);
  }

  /* Front side */
  .card--front { left: 655px; background: var(--card-light); text-align: center; }
  .front__brand-dot {
    position: absolute; left: 138px; top: 92px;
    width: 160px; height: 160px; border-radius: 50%;
    background: var(--brand-grey);
  }
  .front__brand-name {
    position: absolute; left: 0; right: 0; top: 280px;
    font-family: "Exo 2", sans-serif;
    font-weight: 800;
    font-size: 31px;
    line-height: 1.05;
    letter-spacing: 2px;
    color: var(--brand-grey);
  }
  .front__name {
    position: absolute; left: 0; right: 0; top: 384px;
    font-family: "Exo 2", sans-serif; font-weight: 700;
    font-size: 32px; letter-spacing: 2.5px; color: var(--ink);
  }
  .front__email {
    position: absolute; left: 0; right: 0; top: 420px;
    font-size: 18.5px; letter-spacing: 0.8px; color: var(--ink-soft);
  }
  .front__title {
    position: absolute; left: 0; right: 0; top: 444px;
    font-size: 20px; letter-spacing: 4px; color: var(--ink);
  }
  .icons {
    position: absolute; left: 0; right: 0;
    display: flex; justify-content: center; gap: 4px;
  }
  .icons--phone { top: 488px; }
  .icons--place { top: 594px; }
  .icon { width: 35px; height: 35px; }
  .contact {
    position: absolute; left: 0; right: 0;
    font-size: 21px; letter-spacing: 1px; color: var(--ink-soft);
    line-height: 32px;
  }
  .contact--phones { top: 528px; }
  .contact--address { top: 634px; font-size: 19px; line-height: 27px; }
</style>
</head>
<body>
  <section class="card card--back">
    <div class="back__pattern" role="img" aria-label="Embossed repeating pattern of the brand symbol"></div>
    <div class="back__word back__word--top">IRON</div>
    <div class="back__divider">AND</div>
    <div class="back__word back__word--bottom">GRIT</div>
  </section>

  <section class="card card--front">
    <div class="front__brand-dot"></div>
    <div class="front__brand-name">IRON<br>AND GRIT</div>

    <h1 class="front__name">MARCUS DELANEY</h1>
    <p class="front__email">mdelaney@ironandgritapparel.com</p>
    <p class="front__title">FOUNDER &amp; CEO</p>

    <div class="icons icons--phone">
      <svg class="icon" viewBox="0 0 36 36" aria-hidden="true">
        <circle cx="18" cy="18" r="18" fill="#1e1e1e"/>
        <path d="M13.2 10.5l2.6-.5 1.5 3.8-1.8 1.4c.9 2 2.5 3.6 4.5 4.5l1.4-1.8 3.8 1.5-.5 2.6c-.2.9-1 1.5-1.9 1.4-6-.6-10.8-5.4-11.4-11.4-.1-.9.5-1.7 1.4-1.9z" fill="#fff"/>
      </svg>
      <svg class="icon" viewBox="0 0 36 36" aria-hidden="true">
        <circle cx="18" cy="18" r="18" fill="#1e1e1e"/>
        <rect x="13" y="9" width="10" height="18" rx="2" fill="none" stroke="#fff" stroke-width="1.8"/>
        <circle cx="18" cy="23.5" r="1" fill="#fff"/>
      </svg>
    </div>
    <p class="contact contact--phones">1 (888) 555-0142 Ext. 700<br>(281) 555-0187</p>

    <div class="icons icons--place">
      <svg class="icon" viewBox="0 0 36 36" aria-hidden="true">
        <circle cx="18" cy="18" r="18" fill="#1e1e1e"/>
        <path d="M18 8a6.5 6.5 0 0 0-6.5 6.5c0 4.8 6.5 12.5 6.5 12.5s6.5-7.7 6.5-12.5A6.5 6.5 0 0 0 18 8z" fill="#fff"/>
        <circle cx="18" cy="14.5" r="2.4" fill="#1e1e1e"/>
      </svg>
    </div>
    <p class="contact contact--address">4820 N Ridge Ave. Ste. 210<br>Phoenix, AZ 85018</p>
  </section>
</body>
</html>
```